Business card for job seeker professional

Hi. I'm a sale and marketing professional who's just moved to Australia and looking for a job. I would like to have a business card designed for me, which I can use for job interviews/networking. Given ProNexa increasing importance in the job market, I would like my public profile link (http://au.pronexa-example.com/in/tomasveldran/) to be incorporated into my details.

```html
<!DOCTYPE html>
<html lang="en">
<head>
<meta charset="utf-8">
<title>Tomas Veldran – Business Card</title>
<link href="https://fonts.googleapis.com/css2?family=Open+Sans:wght@300;400&display=swap" rel="stylesheet">
<style>
  :root {
    --stage: #e9e6e2;
    --card-dark: #2b3133;
    --card-light: #ffffff;
    --text-light: #ffffff;
    --text-muted: #80878a;
    --text-vertical: #8d9497;
    --accent-orange: #e3702c;
    --accent-blue: #1a6fb0;
    --text-dark: #222222;
  }
  * { box-sizing: border-box; margin: 0; padding: 0; }
  html, body {
    width: 1200px; height: 748px; overflow: hidden;
    background: var(--stage);
    font-family: "Open Sans", Arial, sans-serif;
  }
  .canvas { position: relative; width: 1200px; height: 748px; }
  .card {
    position: absolute; left: 330px; width: 540px; height: 309px;
    box-shadow: 0 2px 10px rgba(0,0,0,.18);
    overflow: hidden;
  }
  /* Front */
  .card--front { top: 55px; background: var(--card-dark); }
  .profile-link {
    position: absolute; left: 19px; top: 298px;
    transform: rotate(-90deg); transform-origin: left top;
    display: flex; align-items: center; gap: 7px;
    height: 18px;
    white-space: nowrap;
  }
  .profile-link__network {
    display: flex; align-items: center; gap: 5px;
    font-size: 10.5px; color: var(--text-vertical);
  }
  .profile-link__dot {
    width: 16px; height: 16px; border-radius: 50%;
    background: var(--accent-blue);
  }
  .profile-link__url {
    font-size: 10.5px; letter-spacing: .2px; color: var(--text-vertical);
  }
  .front__name {
    position: absolute; left: 240px; top: 158px;
    font-size: 32px; font-weight: 400; color: var(--text-light);
    letter-spacing: .2px;
  }
  .front__name-dot {
    display: inline-block; width: 6px; height: 6px; border-radius: 50%;
    background: var(--accent-orange);
    vertical-align: top; margin-top: 6px; margin-left: 1px;
  }
  .front__skills {
    position: absolute; left: 240px; top: 212px;
    list-style: none; font-size: 16.5px; line-height: 27px;
    color: var(--text-muted);
  }
  /* Back */
  .card--back { top: 384px; background: var(--card-light); }
  .back__name {
    position: absolute; left: 51px; top: 165px;
    font-size: 23px; font-weight: 400; color: var(--accent-orange);
  }
  .back__tagline {
    position: absolute; left: 51px; top: 201px; width: 170px;
    font-size: 11.5px; line-height: 14px; color: var(--text-light);
  }
  .back__tagline span {
    background: var(--accent-blue); padding: 0 3px;
    box-decoration-break: clone; -webkit-box-decoration-break: clone;
  }
  .credentials {
    position: absolute; left: 243px; top: 173px; width: 246px; height: 57px;
    background: var(--accent-blue); border-radius: 0 29px 29px 0;
    display: grid; grid-template-columns: 112px 1fr;
    padding: 6px 8px; row-gap: 6px;
    font-size: 8.6px; line-height: 13px; color: var(--text-light);
  }
  .back__skills {
    position: absolute; left: 0; right: 0; top: 265px;
    text-align: center; font-size: 12px; color: var(--text-dark);
  }
</style>
</head>
<body>
<main class="canvas">
  <section class="card card--front" aria-label="Card front">
    <div class="profile-link">
      <span class="profile-link__network"><span class="profile-link__dot"></span>ProNexa</span>
      <span class="profile-link__url">au.pronexa-example.com/in/tomasveldran/</span>
    </div>
    <h1 class="front__name">Tomas Veldran<span class="front__name-dot"></span></h1>
    <ul class="front__skills">
      <li>| Business Strategy</li>
      <li>| International Business Development</li>
      <li>| Marketing and Communication</li>
    </ul>
  </section>

  <section class="card card--back" aria-label="Card back">
    <h2 class="back__name">Tomas Veldran</h2>
    <p class="back__tagline"><span>International trade, sales and marketing professional</span></p>
    <div class="credentials">
      <span>MBA</span>
      <span>Management Consulting</span>
      <span>Bacholor of Science,<br>Mechanical Engineering</span>
      <span>Melbourne Area,<br>Australia</span>
    </div>
    <p class="back__skills">Business Strategy | International Business Development | Marketing and Communication</p>
  </section>
</main>
</body>
</html>
```